Bright Path Crest Home Realty yard sign Logo

UPDATE Design logo for Realty yard sign. 24x24 diamond or 36x24 Rectangle.
Open to all ideas. We are a discount firm but want to project a high end feel. We provide 100% of all services and extensive marketing for 1/2 the fee.
The following info must be on sign
BRIGHT PATH CREST (OR 1/3) HOME REALTY
Dennis Morrow 492-7306
CresthomeQV.com

Target Market(s)

home sellers and buyers

Industry/Entity Type

Real Estate yard sign please see sign attached in gif

Logo Text

Bright Path Crest Home Realty OR (1/3 IN PLACE OF CREST)

Requirements
Must have
• BRIGHT PATH CREST (OR 1/3) HOME REALTY Dennis Morrow 492-7306 CresthomeQV.com FOR SALE (optional)

```html
<!DOCTYPE html>
<html lang="en">
<head>
<meta charset="utf-8">
<title>Bright Path Crest Home Realty – Yard Sign</title>
<link rel="stylesheet" href="https://fonts.googleapis.com/css2?family=Archivo:wdth,wght@125,800;125,900&family=Montserrat:wght@700&display=swap">
<style>
  :root {
    --canvas: #ffffff;
    --sign-black: #000000;
    --brand-yellow: #ffff00;
    --sign-white: #ffffff;
  }
  html, body {
    margin: 0;
    padding: 0;
    width: 1200px;
    height: 900px;
    overflow: hidden;
    background: var(--canvas);
  }
  .canvas {
    position: relative;
    width: 1200px;
    height: 900px;
    background: var(--canvas);
  }
  .yard-sign {
    position: absolute;
    left: 327px;
    top: 177px;
    width: 549px;
    height: 549px;
    background: var(--sign-black);
  }
  .yard-sign svg {
    display: block;
    width: 549px;
    height: 549px;
  }
  .wordmark {
    font-family: "Archivo", "Arial Black", sans-serif;
    font-stretch: 125%;
    font-weight: 900;
    fill: var(--brand-yellow);
  }
  .contact {
    font-family: "Montserrat", "Helvetica Neue", Arial, sans-serif;
    font-weight: 700;
    text-anchor: middle;
  }
  .agent-line { fill: var(--sign-white); font-size: 31px; }
  .web-line { fill: var(--brand-yellow); font-size: 46px; }
  .status-line { fill: var(--sign-white); font-size: 42px; letter-spacing: 1px; }
</style>
</head>
<body>
  <main class="canvas">
    <section class="yard-sign" aria-label="Bright Path Crest Home Realty for sale sign">
      <svg viewBox="0 0 549 549" xmlns="http://www.w3.org/2000/svg">
        <g class="wordmark">
          <text x="57" y="99" font-size="81" textLength="438" lengthAdjust="spacingAndGlyphs">BRIGHT</text>
          <text x="57" y="169" font-size="62" textLength="438" lengthAdjust="spacingAndGlyphs">PATH CREST</text>
          <text x="57" y="250" font-size="66" textLength="438" lengthAdjust="spacingAndGlyphs">HOME REALTY</text>
        </g>
        <g class="contact">
          <text class="agent-line" x="274.5" y="371">Dennis Morrow 492-7306</text>
          <text class="web-line" x="274.5" y="439">CresthomeQV.com</text>
          <text class="status-line" x="274.5" y="509">FOR SALE</text>
        </g>
      </svg>
    </section>
  </main>
</body>
</html>
```